Anzeigengestaltung für Immobilienmakler
Zielgruppe
Wir sind ein Immobilienmakler. Wir wollen eine Plakatkampagne starten. Dazu brauchen wir ein Plakat.
Ich habe noch ein Foto des Plakats hochgeladen, um die Situation zu verdeutlichen.
Aufgabenstellung
Die Maße sind als Anhang dabei. Außerdem dabei ist ein Beispiel eines unserer Werbeschilder (daraus bitte die Farbgebung übernehmen), sowie unser Logo.
Das Plakat sollte mit einem Spruch sein, gerne mit Witz, pfiffig - einfach ein Hingucker.

```html
<!DOCTYPE html>
<html lang="de">
<head>
<meta charset="utf-8">
<title>Plakat – Jonas Brandt Immobilien</title>
<link rel="stylesheet" href="https://fonts.googleapis.com/css2?family=Montserrat:wght@700&family=Marcellus&display=swap">
<style>
  :root {
    --paper: #ffffff;
    --headline: #7b786c;
    --ink: #1f1d1a;
    --frame: #8a8578;
    --frame-light: rgba(255,255,255,0.6);
    --photo-haze: #e9dfcf;
    --photo-green: #b9b39a;
    --photo-wood: #b08560;
    --photo-mid: #8a6142;
    --photo-dark: #5a3c27;
    --logo: #ffffff;
  }
  * { margin: 0; padding: 0; box-sizing: border-box; }
  html, body {
    width: 1200px;
    height: 806px;
    overflow: hidden;
    background: var(--paper);
  }
  .poster {
    position: relative;
    width: 1200px;
    height: 806px;
    background: var(--paper);
  }
  .poster__photo {
    position: absolute;
    left: 660px; top: 0;
    width: 540px;
    height: 806px;
    background:
      radial-gradient(ellipse 38% 22% at 45% 33%, rgba(245,238,226,0.95) 0%, rgba(245,238,226,0) 100%),
      radial-gradient(ellipse 30% 20% at 20% 28%, rgba(170,175,140,0.55) 0%, rgba(170,175,140,0) 100%),
      linear-gradient(180deg, var(--photo-haze) 0%, var(--photo-green) 22%, var(--photo-wood) 42%, var(--photo-mid) 62%, var(--photo-dark) 85%, #4a3120 100%);
  }
  .poster__frame {
    position: absolute;
    left: 32px; top: 34px;
    width: 628px; height: 738px;
    border: 2px solid var(--frame);
    border-right: none;
  }
  .poster__frame--photo {
    left: 660px;
    width: 508px;
    border: 2px solid var(--frame-light);
    border-left: none;
  }
  .headline {
    position: absolute;
    left: 74px; top: 100px;
    font-family: "Montserrat", sans-serif;
    font-weight: 700;
    font-size: 88px;
    line-height: 100px;
    letter-spacing: 1px;
    color: var(--headline);
    text-transform: uppercase;
  }
  .subline {
    position: absolute;
    left: 74px; top: 506px;
    font-family: "Marcellus", serif;
    font-size: 56px;
    line-height: 76px;
    color: var(--ink);
  }
  .website {
    position: absolute;
    right: 680px; top: 694px;
    font-family: "Marcellus", serif;
    font-size: 20px;
    color: var(--ink);
  }
  .brand {
    position: absolute;
    left: 660px; width: 540px;
    top: 596px;
    display: flex;
    flex-direction: column;
    align-items: center;
    font-family: "Marcellus", serif;
    color: var(--logo);
  }
  .brand__mark {
    width: 58px; height: 58px;
    border-radius: 50%;
    background: var(--logo);
    margin-bottom: 18px;
  }
  .brand__name {
    font-size: 48px;
    line-height: 54px;
    letter-spacing: 1px;
  }
  .brand__trade {
    display: flex;
    align-items: center;
    gap: 16px;
    font-size: 20px;
    letter-spacing: 4px;
    line-height: 32px;
  }
  .brand__rule {
    width: 70px; height: 1px;
    background: var(--logo);
  }
</style>
</head>
<body>
  <main class="poster">
    <div class="poster__photo" role="img" aria-label="Foto: kleines Modellhaus mit Lupe auf einem Holztisch, warme Brauntöne, unscharfer Hintergrund"></div>

    <div class="poster__frame"></div>
    <div class="poster__frame poster__frame--photo"></div>

    <h1 class="headline">Hoscht a<br>Häusle<br>zom<br>verkaufa?</h1>
    <p class="subline">KOI PROBLEM -<br>MIR HELFED DR!</p>
    <p class="website">www.jbrandt-immobilien.de</p>

    <div class="brand">
      <span class="brand__mark"></span>
      <p class="brand__name">JONAS BRANDT</p>
      <p class="brand__trade"><span class="brand__rule"></span>IMMOBILIEN<span class="brand__rule"></span></p>
    </div>
  </main>
</body>
</html>
```